Stationery design for software development / consultancy company

We need stationary design based on company logo.

We are based in London, UK and we are providing integration solutions development / consultancy services for VEQ integration projects across UK.

Our name refers two words - integration and grace - and it shows our clients our main specialization field and key characteristics of our solutions / products. We also would like to be associated with follow words: smart, reliable, unique.

Project delivery should include:
- Powerpoint template (needs to have a Cover Page, Table of Contents, 1-2 sample pages, and a Closing/Summary slide at the end)
- Letterhead A4 (Word template)
- Standard invoice A4 (Word template)
- With Compliments Slips A5 (Word template)
- Business card (adobe illustrator)

Attached is logo in vector (please use logo with white background!) and company details for printed stationery.

highly skilled IT professionals

Software

• Clear background in all A4/A5 documents.
All text should be editable, i.e. I will need sources.
• I would prefer light, web 2.0 style colours, follow are in my main interest:
- combination of light grey and orange
- Logo colours
• Please no watermarks on printed stationary

```html
<!DOCTYPE html>
<html lang="en">
<head>
<meta charset="utf-8">
<title>Veloran presentation template</title>
<link rel="stylesheet" href="https://fonts.googleapis.com/css2?family=Open+Sans:wght@400;600;700&family=Arimo:wght@400&display=swap">
<style>
  :root {
    --stage: #2e2e2e;
    --blue-dark: #4a77b8;
    --blue-mid: #6a8fc6;
    --blue-light: #8fabd4;
    --body-top: #dfe3e7;
    --body-bottom: #f4f5f6;
    --footer-grey: #a9acaf;
    --footer-green: #93bb4d;
    --title-ink: #2f3136;
    --sub-ink: #5c6066;
    --copy-ink: #2b4270;
    --step-green: #3fae2a;
    --step-green-light: #8fdc6a;
    --step-box: #f2f3f4;
    --step-edge: #b9bcc0;
    --contact-ink: #1c1c1c;
    --brand-ink: #565a60;
    --brand-dot: #3f8fd0;
  }
  * { box-sizing: border-box; margin: 0; padding: 0; }
  html, body { width: 1200px; height: 900px; overflow: hidden; }
  body { background: var(--stage); position: relative; font-family: "Open Sans", Arial, sans-serif; }

  .slide { position: absolute; width: 570px; height: 430px; overflow: hidden;
    background: linear-gradient(180deg, var(--body-top), var(--body-bottom)); }
  .slide-footer { position: absolute; left: 0; right: 0; bottom: 0; height: 14px;
    background: linear-gradient(180deg, #c4c7ca, var(--footer-grey)); }

  /* Cover */
  .cover { left: 16px; top: 10px; }
  .cover-band { position: absolute; left: 0; top: 0; width: 100%; height: 250px;
    background: linear-gradient(180deg, var(--blue-dark), var(--blue-mid) 70%, var(--blue-light)); }
  .cover-visual { position: absolute; left: 300px; top: 130px; width: 220px; height: 200px;
    background: radial-gradient(closest-side, #e2e5e8 0%, #a9aeb4 45%, rgba(130,136,142,0.55) 75%, rgba(130,136,142,0) 100%); }
  .cover-title { position: absolute; left: 30px; top: 292px; font-size: 28px; font-weight: 600; color: var(--title-ink); }
  .cover-sub { position: absolute; left: 34px; top: 330px; font-size: 18px; color: var(--sub-ink); }

  /* Content */
  .content { left: 614px; top: 10px; }
  .content-header { position: absolute; left: 0; top: 0; width: 100%; height: 50px;
    background: linear-gradient(180deg, var(--blue-dark), var(--blue-mid));
    color: #fff; font-weight: 700; font-size: 27px; text-align: center; line-height: 50px; }
  .search-visual { position: absolute; left: 20px; top: 96px; width: 130px; height: 130px;
    background: radial-gradient(closest-side, #eef5fb 0 45%, #9fb6cc 55%, rgba(150,165,180,0.45) 75%, rgba(150,165,180,0) 100%); }
  .step { position: absolute; height: 40px; right: 24px; background: linear-gradient(180deg, #fff, var(--step-box));
    border-bottom: 3px solid var(--step-edge); font-size: 10px; line-height: 13px; color: #333; padding: 7px 8px 0 40px; }
  .step-1 { left: 196px; top: 210px; }
  .step-2 { left: 286px; top: 160px; }
  .step-3 { left: 366px; top: 114px; }
  .step-badge { position: absolute; width: 40px; height: 40px; border-radius: 50%;
    background: radial-gradient(circle at 40% 30%, var(--step-green-light), var(--step-green) 65%);
    color: #1a3a10; font-weight: 700; font-size: 18px; text-align: center; line-height: 40px; }
  .badge-1 { left: 200px; top: 176px; }
  .badge-2 { left: 290px; top: 126px; }
  .badge-3 { left: 374px; top: 82px; }
  .content-copy { position: absolute; left: 24px; top: 298px; width: 522px; font-size: 12.4px; line-height: 17.6px;
    color: var(--copy-ink); text-align: justify; }

  /* Closing */
  .closing { left: 322px; top: 454px; }
  .closing-header { position: absolute; left: 0; top: 0; width: 100%; height: 60px;
    background: linear-gradient(180deg, var(--blue-dark), var(--blue-mid));
    color: #fff; font-family: "Arimo", Arial, sans-serif; font-weight: 400; font-size: 24px; text-align: center; line-height: 60px; }
  .brand { position: absolute; left: 44px; top: 196px; display: flex; align-items: center; gap: 10px; }
  .brand-dot { width: 34px; height: 34px; border-radius: 50%; background: var(--brand-dot); }
  .brand-name { font-family: "Arimo", Arial, sans-serif; font-size: 38px; color: var(--brand-ink); }
  .contact { position: absolute; left: 314px; top: 146px; font-family: "Arimo", Arial, sans-serif;
    font-size: 14px; line-height: 18px; color: var(--contact-ink); font-style: normal; }
  .contact-links { margin-top: 6px; }
  .closing .slide-footer { height: 24px; background: var(--footer-green); }
</style>
</head>
<body>

<section class="slide cover">
  <div class="cover-band"></div>
  <div class="cover-visual" role="img" aria-label="Laptop computer illustration"></div>
  <h1 class="cover-title">Presentation Title</h1>
  <p class="cover-sub">The sub heading goes here</p>
  <div class="slide-footer"></div>
</section>

<section class="slide content">
  <h2 class="content-header">TITLE</h2>
  <div class="search-visual" role="img" aria-label="Magnifying glass illustration"></div>
  <div class="step step-1">Go ahead and replace it with your own text. This is an example text.</div>
  <div class="step step-2">Go ahead and replace it with your own text. This is an example text.</div>
  <div class="step step-3">Go ahead and replace it with your own text.</div>
  <div class="step-badge badge-1">1</div>
  <div class="step-badge badge-2">2</div>
  <div class="step-badge badge-3">3</div>
  <p class="content-copy">Lorem ipsum dolor sit amet, consectetur adipiscing elit. Curabitur sodales odio vitae mi tempus id luctus ligula commodo. Vestibulum sit amet aliquam diam. Morbi a libero ut ligula fermentum lacinia non vitae purus. Ut vel orci felis. In hac habitasse platea dictumst. Duis posuere suscipit ante, eget fermentum est porta at. Nulla pretium, massa fermentum tempus suscipit, metus leo hendrerit purus, eu elementum mauris lorem eu dolor. Pellentesque porta semper odio eget bibendum. In at tortor urna, eu tristique mi.</p>
  <div class="slide-footer"></div>
</section>

<section class="slide closing">
  <h2 class="closing-header">THANK YOU FOR YOU TIME</h2>
  <div class="brand">
    <span class="brand-dot"></span>
    <span class="brand-name">veloran</span>
  </div>
  <address class="contact">
    Veloran Limited<br>
    42 Marlow Court<br>
    88 Kingsbridge Road<br>
    London<br>
    SW9 4QT<br>
    United Kingdom
    <div class="contact-links">
      Web : www.veloran.co.uk<br>
      Email : enquiries@veloran.co.uk<br>
      Tel : +44(0)20 7946 0321
    </div>
  </address>
  <div class="slide-footer"></div>
</section>

</body>
</html>
```